Music Industry Business Needs a Business Card Design

Copper Lantern is an audio mastering company that has been in business for 20 years. Mastering is the final creative step in the music production chain. Our job is to make the music sound as good as it possibly can prior to release to the public. Our world is technical, artistic, precise. We work on everything from independent artists to the music for the Grandfield Cup. We are looking for a new, more modern business card design. I am uploading a copy of our logo, although it doesn't absolutely need to be included in the design.

Target Market(s)

Music Industry Professionals

Industry/Entity Type

Business

Contact Information for Business Card

Address, Phone, Email, Website, Name, Job Title

Font styles to use
Sans Serif

Requirements
Must have
• Sorry, but I don't have any concrete things to request. If I had a clear idea of what I want, I would probably just design something myself. I am looking for fresh input and thought I would try this.
Should not have
• Anything that is typical, such as headphones or the like.

```html
<!DOCTYPE html>
<html lang="en">
<head>
<meta charset="utf-8">
<title>Copper Lantern – Business Card</title>
<link href="https://fonts.googleapis.com/css2?family=Roboto+Condensed:wght@300;400;700&display=swap" rel="stylesheet">
<style>
  :root {
    --page-bg: #e9e7e3;
    --card-bg: #2b2b2b;
    --accent: #8dc63f;
    --text-light: #f2f2f2;
    --text-muted: #d9d9d9;
  }
  * { box-sizing: border-box; margin: 0; padding: 0; }
  html, body {
    width: 1200px; height: 720px; overflow: hidden;
    background: var(--page-bg);
    font-family: "Roboto Condensed", "Arial Narrow", sans-serif;
  }
  .card {
    position: absolute; left: 75px; top: 60px;
    width: 1050px; height: 600px;
    background: var(--card-bg);
    box-shadow: 0 12px 30px rgba(0,0,0,.25);
    overflow: hidden;
  }
  .card-graphics { position: absolute; left: 0; top: 0; }
  .brand-name {
    position: absolute; left: 0; width: 100%; top: 110px;
    text-align: center; padding-left: 60px;
    font-weight: 300; font-size: 56px; letter-spacing: 1px; line-height: 1;
    color: var(--text-light); text-transform: uppercase; white-space: nowrap;
  }
  .website {
    position: absolute; top: 208px; left: 0; width: 100%;
    text-align: center; padding-left: 120px;
    font-size: 21px; font-weight: 700; line-height: 1; color: var(--text-muted);
  }
  .person {
    position: absolute; left: 52px; top: 282px;
    border-left: 7px solid var(--accent);
    padding-left: 16px;
  }
  .person-name { font-size: 44px; font-weight: 700; color: var(--text-light); line-height: 1.05; white-space: nowrap; }
  .person-title { font-size: 22px; font-weight: 400; color: var(--text-muted); margin-top: 4px; }
  .tagline {
    position: absolute; left: 330px; top: 298px;
    font-size: 30px; font-weight: 700; line-height: 1; color: var(--accent);
    text-transform: uppercase; white-space: nowrap;
  }
  .address {
    position: absolute; left: 300px; top: 446px;
    font-size: 28px; font-weight: 700; line-height: 1.1; color: var(--text-light); white-space: nowrap;
  }
  .email, .phone {
    position: absolute; display: flex; align-items: center; gap: 10px;
    font-weight: 700; line-height: 1; color: var(--text-light); white-space: nowrap;
  }
  .email { left: 745px; top: 518px; font-size: 22px; }
  .phone { left: 170px; top: 500px; font-size: 30px; }
</style>
</head>
<body>
  <main class="card">
    <svg class="card-graphics" width="1050" height="600" viewBox="0 0 1050 600" aria-hidden="true">
      <g class="equalizer" fill="var(--accent)">
        <rect x="340" y="405" width="7" height="25"/><rect x="352" y="380" width="7" height="50"/>
        <rect x="364" y="400" width="7" height="30"/><rect x="376" y="370" width="7" height="60"/>
        <rect x="388" y="392" width="7" height="38"/><rect x="400" y="415" width="7" height="15"/>
        <rect x="412" y="378" width="7" height="52"/><rect x="424" y="398" width="7" height="32"/>
        <rect x="436" y="366" width="7" height="64"/><rect x="448" y="388" width="7" height="42"/>
        <rect x="460" y="374" width="7" height="56"/><rect x="472" y="396" width="7" height="34"/>
        <rect x="484" y="382" width="7" height="48"/><rect x="496" y="368" width="7" height="62"/>
        <rect x="508" y="400" width="7" height="30"/><rect x="520" y="386" width="7" height="44"/>
        <rect x="532" y="372" width="7" height="58"/><rect x="544" y="394" width="7" height="36"/>
        <rect x="556" y="380" width="7" height="50"/><rect x="568" y="364" width="7" height="66"/>
        <rect x="580" y="390" width="7" height="40"/><rect x="592" y="376" width="7" height="54"/>
        <rect x="604" y="360" width="7" height="70"/><rect x="616" y="382" width="7" height="48"/>
        <rect x="628" y="366" width="7" height="64"/><rect x="640" y="356" width="7" height="74"/>
        <rect x="652" y="374" width="7" height="56"/><rect x="664" y="362" width="7" height="68"/>
        <rect x="676" y="354" width="7" height="76"/><rect x="688" y="370" width="7" height="60"/>
        <rect x="700" y="358" width="7" height="72"/><rect x="712" y="352" width="7" height="78"/>
        <rect x="724" y="366" width="7" height="64"/><rect x="736" y="354" width="7" height="76"/>
        <rect x="748" y="350" width="7" height="80"/><rect x="760" y="330" width="7" height="100"/>
        <rect x="772" y="300" width="7" height="130"/><rect x="784" y="280" width="7" height="150"/>
        <rect x="796" y="310" width="7" height="120"/><rect x="808" y="290" width="7" height="140"/>
        <rect x="820" y="250" width="7" height="180"/><rect x="832" y="300" width="7" height="130"/>
        <rect x="844" y="360" width="7" height="70"/><rect x="856" y="412" width="7" height="18"/>
      </g>
      <rect class="baseline" x="0" y="430" width="900" height="3" fill="var(--accent)"/>
      <polygon class="contact-wedge" points="380,555 1050,470 1050,555" fill="var(--accent)"/>
      <rect class="bottom-band" x="0" y="566" width="1050" height="34" fill="var(--accent)"/>
    </svg>

    <div class="brand-name">Copper Lantern</div>
    <div class="website">www.copperlantern.ca</div>

    <div class="person">
      <div class="person-name">Noel Ardent</div>
      <div class="person-title">CEO</div>
    </div>

    <div class="tagline">Finest Quality Audio Mastering</div>

    <div class="address">48 Marlow Terrace, Kelvin Grove, QLD, 4059</div>

    <div class="email">
      <svg width="22" height="16" viewBox="0 0 22 16" aria-hidden="true">
        <rect x="0" y="0" width="22" height="16" fill="var(--card-bg)"/>
        <path d="M2 2 L11 9 L20 2" stroke="var(--accent)" stroke-width="2" fill="none"/>
      </svg>
      noel@copperlantern.com
    </div>

    <div class="phone">
      <svg width="22" height="26" viewBox="0 0 22 26" aria-hidden="true">
        <path d="M5 2 C2 4 1 8 3 13 C5 18 9 22 14 24 C17 25 19 23 20 21 L16 17 C15 18 13 19 12 18 C9 16 7 12 7 10 C7 9 8 8 9 7 Z" fill="var(--accent)"/>
      </svg>
      +914-555-0173
    </div>
  </main>
</body>
</html>
```